Venture Wreckers Book Needs a Cover Design

We need a cover design for Venture Wreckers, Practical Guidance for Faltering Ventures and Doubting Company Founders. We will publish and ebook first (first priority), followed by a hard cover printed book, and then a soft cover book after a few months. The book includes 40 Venture Wreckers and actions owners can implement to counter them and grow. Some examples of killers: self-sabotage, wild optimism, scamming, addictions, burnout, no plan, procrastination, recklessness, haemorrhaging money, etc. We plan to publish the ebook to Pagelume / Tarvelo standards. We want to see designs that convey professionalism, simplicity and creativity.

Target Market(s)

Small and microbusinesses, including start-ups, proprietorships, cottage industries, home-based, single operator, and businesses with or without employees, including corporations and partnerships with fewer than five employees

Industry/Entity Type

Business

Font styles to use
Sans Serif

Colors

Designer to choose colors to be used in the design.

Requirements
Must have
• Uncluttered, professional
• Title: Venture Wreckers
• Subtitle: Practical Guidance for Faltering Ventures and Doubting Company Founders
• Author: Mel Hartigan
Nice to have
• n/a

```html
<!DOCTYPE html>
<html lang="en">
<head>
<meta charset="utf-8">
<title>Venture Wreckers — Book Cover</title>
<link rel="stylesheet" href="https://fonts.googleapis.com/css2?family=Noto+Serif:ital,wght@0,400;0,700;1,700&display=swap">
<style>
  :root {
    --page-bg: #ffffff;
    --green-deep: #127a33;
    --green-mid: #1f9a48;
    --green-glow: #3fdc7c;
    --green-stripe: #46e884;
    --teal-photo-top: #5fd39b;
    --teal-photo-mid: #2aa868;
    --teal-photo-low: #1e7f4f;
    --title-white: #ffffff;
    --subtitle-ink: #0b0b0b;
  }
  * { margin: 0; padding: 0; box-sizing: border-box; }
  html, body {
    width: 960px; height: 1200px; overflow: hidden;
    background: var(--page-bg);
  }
  .book-cover {
    position: absolute;
    left: 100px; top: 30px;
    width: 760px; height: 1140px;
    overflow: hidden;
    background: var(--green-mid);
  }
  .cover-photo {
    position: absolute;
    left: 0; top: 340px;
    width: 760px; height: 740px;
    background:
      radial-gradient(ellipse at 50% 45%, var(--teal-photo-top) 0%, var(--teal-photo-mid) 55%, var(--teal-photo-low) 100%);
  }
  .cover-shapes {
    position: absolute; inset: 0;
    width: 760px; height: 1140px;
  }
  .cover-title {
    position: absolute;
    left: 0; top: 110px; width: 760px;
    text-align: center;
    font-family: "Noto Serif", serif;
    font-weight: 400;
    font-size: 118px;
    line-height: 122px;
    color: var(--title-white);
    letter-spacing: 1px;
  }
  .cover-subtitle {
    position: absolute;
    left: 60px; top: 590px; width: 640px;
    text-align: center;
    font-family: "Noto Serif", serif;
    font-style: italic;
    font-weight: 700;
    font-size: 27px;
    line-height: 30px;
    color: var(--subtitle-ink);
    transform: rotate(-3deg);
  }
  .cover-author {
    position: absolute;
    left: 0; top: 1078px; width: 760px;
    text-align: center;
    font-family: "Noto Serif", serif;
    font-weight: 400;
    font-size: 30px;
    letter-spacing: 1px;
    color: var(--title-white);
    text-transform: uppercase;
  }
</style>
</head>
<body>
  <main class="book-cover">
    <div class="cover-photo" role="img" aria-label="Photo of a young entrepreneur working on a laptop at a desk, set against a green globe grid of binary code"></div>

    <svg class="cover-shapes" viewBox="0 0 760 1140" aria-hidden="true">
      <defs>
        <radialGradient id="topGlow" cx="0.62" cy="0.55" r="0.7">
          <stop offset="0" stop-color="var(--green-glow)"/>
          <stop offset="0.55" stop-color="var(--green-mid)"/>
          <stop offset="1" stop-color="var(--green-deep)"/>
        </radialGradient>
        <linearGradient id="bottomBand" x1="0" y1="0" x2="0" y2="1">
          <stop offset="0" stop-color="var(--green-mid)"/>
          <stop offset="1" stop-color="var(--green-deep)"/>
        </linearGradient>
      </defs>

      <!-- upper title field -->
      <path class="title-field" d="M0 0 H760 V370 C640 300 560 300 470 360 C360 430 220 520 0 490 Z" fill="url(#topGlow)"/>
      <!-- wave stripes -->
      <path class="wave-stripe" d="M0 500 C220 530 360 440 470 372 C560 314 640 312 760 382" fill="none" stroke="var(--green-stripe)" stroke-width="14"/>
      <path class="wave-stripe-dark" d="M0 516 C220 548 360 458 470 390 C560 334 640 332 760 400" fill="none" stroke="var(--green-deep)" stroke-width="8"/>
      <path class="wave-stripe-soft" d="M0 530 C220 562 360 472 470 404 C560 350 640 348 760 414" fill="none" stroke="var(--green-glow)" stroke-width="4" opacity="0.8"/>

      <!-- lower author band -->
      <path class="author-band" d="M0 1062 C200 1040 520 1050 760 1066 V1140 H0 Z" fill="url(#bottomBand)"/>
      <path class="band-stripe" d="M0 1056 C200 1034 520 1044 760 1060" fill="none" stroke="var(--green-stripe)" stroke-width="8"/>
      <path class="band-stripe-dark" d="M0 1044 C200 1022 520 1032 760 1048" fill="none" stroke="var(--green-deep)" stroke-width="5"/>
    </svg>

    <h1 class="cover-title">Venture<br>Wreckers</h1>
    <p class="cover-subtitle">Practical Guidance for Faltering Ventures<br>and Doubting Company Founders</p>
    <p class="cover-author">Mel Hartigan</p>
  </main>
</body>
</html>
```